Flyer for Custom Home Builder!

my company is Harlow Ridge Homes, I am looking for a flyer that we can send via email to a customer, or print and hand out. I am thinking four pages so we could print this and fold it., possibly creating a folder. The name of the company is Harlow Ridge Homes our website is here www.harlowridgehomes-example.com. Some text you can use "Crafting luxury homes isn't just a job, it's our passion.
With meticulous attention to detail and an unwavering commitment to using the finest materials, Harlow Ridge Homes consistently delivers exceptional results that stand as a testament to our commitment to quality."

"Trust is the cornerstone of our foundation.
With a proven track record of delivering on our promises for over 16 years, we prioritize transparent communication and integrity throughout every step of the home-building journey".

you may need to obtain the photos here
https://files.example-share.net/f/k27pw4m8zrt03xq61bnv/h?key=48vn2c9q1x7mb5t0ekd3h&dl=0

Target Market(s)

We build homes for every wealthy clients, therefore the photos are extremely important

Industry/Entity Type

Construction.

Requirements
Must have
• clear larger photos

```html
<!DOCTYPE html>
<html lang="en">
<head>
<meta charset="UTF-8">
<title>Harlow Ridge Homes – Flyer</title>
<link href="https://fonts.googleapis.com/css2?family=Bebas+Neue&family=Montserrat:wght@400;600;700&display=swap" rel="stylesheet">
<style>
  :root {
    --ink: #1a1a1a;
    --panel: #1b1b1b;
    --paper: #ffffff;
    --page-bg: #ffffff;
    --logo-grey: #3a3a3a;
    --logo-sub: #9a9a9a;
    --on-dark: #f2f2f2;
  }
  * { margin: 0; padding: 0; box-sizing: border-box; }
  html, body {
    width: 674px; height: 1200px; overflow: hidden;
    background: var(--page-bg);
  }
  .flyer {
    position: absolute; left: 17px; top: 186px;
    width: 640px; height: 828px;
    background: var(--paper);
    box-shadow: 0 2px 8px rgba(0,0,0,0.25);
    overflow: hidden;
  }
  .brand {
    position: absolute; left: 44px; top: 50px; width: 200px;
  }
  .brand-name {
    font-family: "Bebas Neue", sans-serif;
    font-size: 34px; line-height: 30px; letter-spacing: 1px;
    color: var(--logo-grey);
  }
  .info-panel {
    position: absolute; left: 0; top: 113px;
    width: 298px; height: 518px;
    background: var(--panel);
    color: var(--on-dark);
  }
  .headline {
    position: absolute; left: 44px;
    font-family: "Bebas Neue", sans-serif;
    font-weight: 400; color: var(--on-dark);
  }
  .headline--passion { top: 26px; font-size: 42px; line-height: 38px; }
  .headline--trust { top: 303px; font-size: 37px; line-height: 37px; }
  .body-copy {
    position: absolute; left: 44px; width: 236px;
    font-family: "Montserrat", sans-serif;
    font-size: 10px; line-height: 12.6px;
  }
  .body-copy--passion { top: 188px; font-weight: 400; }
  .body-copy--trust { top: 430px; font-weight: 600; text-align: justify; text-align-last: left; }
  .divider {
    position: absolute; left: 44px; top: 279px;
    width: 228px; height: 2px; background: var(--on-dark);
  }
  .contact {
    position: absolute; left: 0; top: 631px; width: 298px; height: 197px;
    color: var(--ink);
  }
  .contact-title {
    position: absolute; left: 45px; top: 20px;
    font-family: "Montserrat", sans-serif; font-weight: 700;
    font-size: 22px; letter-spacing: 1px;
  }
  .contact-rule {
    position: absolute; left: 0; top: 54px; width: 229px; height: 2px;
    background: var(--ink);
  }
  .contact-row { position: absolute; left: 46px; display: flex; align-items: center; gap: 8px; }
  .contact-row svg { flex: none; }
  .contact-row--phone { top: 66px; }
  .phone-number {
    font-family: "Bebas Neue", sans-serif; font-size: 38px; line-height: 38px;
  }
  .contact-row--address { top: 110px; align-items: flex-start; }
  .contact-row--web { top: 149px; }
  .contact-text {
    font-family: "Montserrat", sans-serif; font-weight: 600;
    font-size: 9.6px; line-height: 12.5px;
  }
  .contact-text--web { font-weight: 400; }
  .photo { position: absolute; left: 302px; width: 338px; }
  .photo--exterior {
    top: 0; height: 199px;
    background: linear-gradient(180deg, #6b5a9a 0%, #c98aa8 22%, #d8cfc4 45%, #8a7e70 75%, #4f5a3c 100%);
  }
  .photo--aerial {
    top: 213px; height: 219px;
    background: linear-gradient(180deg, #7bb2e3 0%, #6f9a4e 28%, #e6e6e2 55%, #4e7a3a 85%, #6a7d4a 100%);
  }
  .photo--interior {
    top: 444px; height: 220px;
    background: linear-gradient(160deg, #e9e9e6 0%, #cfcac2 40%, #a9a197 70%, #d9cfc2 100%);
  }
  .photo--pool {
    top: 680px; height: 148px;
    background: linear-gradient(180deg, #d8d6d0 0%, #8b7a68 35%, #6fb7c6 70%, #9bd2db 100%);
  }
  .photo-rule { position: absolute; left: 302px; width: 338px; height: 5px; background: var(--panel); }
  .photo-rule--first { top: 202px; }
  .photo-rule--second { top: 434px; }
</style>
</head>
<body>
  <main class="flyer">
    <div class="brand">
      <div class="brand-name">Harlow Ridge Homes</div>
    </div>

    <section class="info-panel">
      <h1 class="headline headline--passion">Crafting<br>Luxury Homes<br>Isn't Just a Job<br>It's Our Passion</h1>
      <p class="body-copy body-copy--passion">With meticulous attention to detail and an unwavering commitment to using the finest materials, Harlow Ridge Homes consistently delivers exceptional results that stand as a testament to our commitment to quality.</p>
      <div class="divider"></div>
      <h2 class="headline headline--trust">Trust Is<br>The Cornerstone<br>Of Our Foundation</h2>
      <p class="body-copy body-copy--trust">With a proven track record of delivering on our promises for over 16 years, we prioritize transparent communication and integrity throughout every step of the home-building journey</p>
    </section>

    <section class="contact">
      <h3 class="contact-title">CONTACT US!</h3>
      <div class="contact-rule"></div>
      <div class="contact-row contact-row--phone">
        <svg width="18" height="18" viewBox="0 0 18 18" aria-hidden="true">
          <circle cx="9" cy="9" r="8" fill="none" stroke="#1a1a1a" stroke-width="2"/>
          <path d="M6 5.5c.5-.5 1.2-.4 1.5.1l.7 1.2c.2.4.1.8-.2 1.1l-.5.4c.4 1 1.2 1.8 2.2 2.2l.4-.5c.3-.3.7-.4 1.1-.2l1.2.7c.5.3.6 1 .1 1.5-1 1-2.6.9-4.4-.9S5 6.5 6 5.5z" fill="#1a1a1a"/>
        </svg>
        <span class="phone-number">(555) 014-2870</span>
      </div>
      <div class="contact-row contact-row--address">
        <svg width="12" height="15" viewBox="0 0 12 15" aria-hidden="true">
          <path d="M6 0C2.7 0 0 2.6 0 5.8 0 10 6 15 6 15s6-5 6-9.2C12 2.6 9.3 0 6 0z" fill="#1a1a1a"/>
          <circle cx="6" cy="5.8" r="2.2" fill="#fff"/>
        </svg>
        <span class="contact-text">480 CEDAR BLUFF WAY, SUITE 200<br>LAKEVIEW TX 75000</span>
      </div>
      <div class="contact-row contact-row--web">
        <svg width="13" height="13" viewBox="0 0 13 13" aria-hidden="true">
          <circle cx="6.5" cy="6.5" r="6" fill="#1a1a1a"/>
          <g fill="none" stroke="#fff" stroke-width="0.8">
            <ellipse cx="6.5" cy="6.5" rx="2.6" ry="6"/>
            <line x1="0.5" y1="6.5" x2="12.5" y2="6.5"/>
            <line x1="1.5" y1="3.5" x2="11.5" y2="3.5"/>
            <line x1="1.5" y1="9.5" x2="11.5" y2="9.5"/>
          </g>
        </svg>
        <span class="contact-text contact-text--web">www.harlowridgehomes-example.com</span>
      </div>
    </section>

    <div class="photo photo--exterior" role="img" aria-label="Photo of a large stone luxury home with a paved driveway at dusk under a purple sky"></div>
    <div class="photo-rule photo-rule--first"></div>
    <div class="photo photo--aerial" role="img" aria-label="Aerial photo of a modern white home with a pool surrounded by green trees"></div>
    <div class="photo-rule photo-rule--second"></div>
    <div class="photo photo--interior" role="img" aria-label="Photo of a bright open-plan living and dining room with floor-to-ceiling windows"></div>
    <div class="photo photo--pool" role="img" aria-label="Photo of a modern home's outdoor patio with a turquoise pool and spa"></div>
  </main>
</body>
</html>
```